Varga Lillas Physiotherapy Business Card Vienna

We need a business card design for a newly created Physiotherapy company based in Vienna Austria.
We seek a simple, modern, minimalist design without too much color variation. The font should look young/fresh, but definitely not childish or so. Since we are a starting Business, we currently haven't got a logo, if you feel like a logo would fit your design, feel free to use one, but it's not necessary.
Target Market(s)
Healthcare, young and elderly people with mobility issues
Industry/Entity Type
Health And Wellness
Contact Information for Business Card
Name: Lilla Varga
Title description: Physiotherapist
Phone num: +43 664 5290 4816
e-mail: lilla.praxis@brelomail.com
Colors
Designer to choose colors to be used in the design.
Requirements
Must have
- Final design language must be in German, basically, the Title Description needs to be "Physiotherapeutin" the other details remain as in the English Language.
Nice to have
- Simple, modern, minimalist design
Should not have
- too many colors, Obvious use of a skeleton, skull, spline

```html
<!DOCTYPE html>
<html lang="de">
<head>
<meta charset="utf-8">
<title>Lilla Varga – Physiotherapeutin Visitenkarte</title>
<link rel="stylesheet" href="https://fonts.googleapis.com/css2?family=Montserrat:wght@300;400;700;900&display=swap">
<style>
  :root {
    --stage: #e6e6e6;
    --lime: #b4c13a;
    --lime-light: #c3cd58;
    --lime-deep: #a6b32f;
    --ink: #3b3b3b;
    --paper: #f6f6f6;
    --white: #ffffff;
  }
  * { margin: 0; padding: 0; box-sizing: border-box; }
  html, body { width: 1200px; height: 800px; overflow: hidden; }
  body {
    background: var(--stage);
    font-family: "Montserrat", Arial, sans-serif;
    position: relative;
  }
  .card {
    position: absolute;
    top: 130px;
    width: 330px;
    height: 540px;
    box-shadow: 0 6px 18px rgba(0,0,0,0.12);
  }
  /* Front */
  .card-front { left: 225px; }
  .front-texture {
    position: absolute; inset: 0;
    background: linear-gradient(160deg, var(--lime-deep) 0%, var(--lime) 45%, var(--lime-light) 100%);
  }
  .front-brand {
    position: absolute;
    left: 0; right: 0;
    top: 360px;
    text-align: center;
    color: var(--white);
  }
  .brand-name {
    font-weight: 900;
    font-size: 34px;
    letter-spacing: -0.5px;
    line-height: 1;
    margin-bottom: 16px;
  }
  .brand-line-strong {
    font-weight: 900;
    font-size: 30px;
    line-height: 1;
    letter-spacing: 0.5px;
  }
  .brand-line-light {
    font-weight: 300;
    font-size: 28px;
    line-height: 1.1;
    letter-spacing: 0.5px;
  }
  /* Back */
  .card-back { left: 645px; background: var(--paper); }
  .holder {
    position: absolute;
    left: 36px; top: 70px;
  }
  .holder-name {
    font-weight: 900;
    font-size: 58px;
    line-height: 0.86;
    color: var(--ink);
    text-transform: uppercase;
    letter-spacing: -1px;
  }
  .holder-title {
    display: inline-block;
    margin-top: -6px;
    background: var(--lime);
    color: var(--white);
    font-weight: 400;
    font-size: 25px;
    padding: 2px 10px 4px 6px;
    position: relative;
    z-index: -0;
  }
  .contact {
    position: absolute;
    left: 36px; bottom: 64px;
    list-style: none;
    font-size: 13px;
    color: var(--ink);
  }
  .contact li { display: flex; align-items: center; gap: 8px; line-height: 1.7; }
  .contact svg { width: 13px; height: 13px; fill: var(--lime); flex: none; }
</style>
</head>
<body>
  <section class="card card-front">
    <div class="front-texture" role="img" aria-label="Wiederholtes Monogramm-Muster in Grüntönen"></div>
    <div class="front-brand">
      <div class="brand-name">Lilla Varga</div>
      <div class="brand-line-strong">PHYSIO</div>
      <div class="brand-line-light">THERAPEUTIN</div>
    </div>
  </section>

  <section class="card card-back">
    <div class="holder">
      <h1 class="holder-name">Lilla<br>Varga</h1>
      <div class="holder-title">Physiotherapeutin</div>
    </div>
    <ul class="contact">
      <li>
        <svg viewBox="0 0 24 24" aria-hidden="true"><path d="M6.6 10.8a15.1 15.1 0 0 0 6.6 6.6l2.2-2.2a1 1 0 0 1 1-.25 11.4 11.4 0 0 0 3.6.57 1 1 0 0 1 1 1V20a1 1 0 0 1-1 1A17 17 0 0 1 3 4a1 1 0 0 1 1-1h3.5a1 1 0 0 1 1 1c0 1.25.2 2.45.57 3.57a1 1 0 0 1-.25 1z"/></svg>
        +43 664 5290 4816
      </li>
      <li>
        <svg viewBox="0 0 24 24" aria-hidden="true"><path d="M2 5h20v14H2z M4 7v.5l8 5.5 8-5.5V7z" fill-rule="evenodd"/></svg>
        lilla.praxis@brelomail.com
      </li>
    </ul>
  </section>
</body>
</html>
```